Tri-Fold Behavioral Health (Addiction) Agency Brochure

We need an updated and refreshed brochure design for our Residential Treatment Facilities. These facilities provide residential comprehensive treatment for those struggling with drug and alcohol addiction along with those who are dually diagnosed with mental health issues as well. We are starting with this brochure but plan to have our other brochures "match" the design and will submit that following completion of this design. I have attached a "Brochure Areas" document that is numbered and corresponds to the brochure areas of our current brochure. We have modified the wording in each of these areas so the wording in the attached word document is what needs to go on the design (not the words in the attached pictures of our current brochure). We want something that is a professional design look. The front page of the brochure needs to have our main agency Logo/Name: Maple Hollow Behavioral Health Partners (logo attached). The back page we would like to have the two locations listed with the address (possible map if able). The first is called: The Harbor at Maple Hollow - located at 7214 Tolliver Lane, Frazeysburg OH 43829. The Second Facility is called: The Brennick at Maple Hollow - located at 618 Garvin St, Zanesville OH 43708. I have also attached some pictures of our facilities that can be used. They all don't have to be used and we would still like some stock photos of "people" or group counseling, etc.

Requirements
Must have
• Need final design file to be publisher or word along with pdf and or other print type file.
Nice to have
• I have also attached the current booth design photo that we are using to possibly match design look.

```html
<!DOCTYPE html>
<html lang="en">
<head>
<meta charset="utf-8">
<title>Residential Treatment Brochure – Inside Spread</title>
<link href="https://fonts.googleapis.com/css2?family=Crimson+Pro:wght@600&family=Open+Sans:wght@400;600&display=swap" rel="stylesheet">
<style>
  :root {
    --page-bg: #e9e6e1;
    --box-blue: rgba(46, 137, 196, 0.86);
    --box-blue-solid: #2f89c1;
    --wave-blue: #2f8ac4;
    --wave-green: #3a8a2c;
    --navy: #1d2434;
    --white: #ffffff;
  }
  * { margin: 0; padding: 0; box-sizing: border-box; }
  html, body { width: 1200px; height: 1200px; overflow: hidden; background: var(--page-bg); }
  .spread {
    position: absolute; left: 0; top: 136px;
    width: 1200px; height: 927px;
    overflow: hidden; background: var(--white);
    box-shadow: 0 4px 18px rgba(0,0,0,0.18);
  }
  .photo { position: absolute; }
  .photo--forest {
    left: 0; top: 0; width: 400px; height: 640px;
    background: linear-gradient(180deg, #6f7a72 0%, #93a19a 35%, #55625a 70%, #2f3a33 100%);
  }
  .photo--sunset {
    left: 400px; top: 370px; width: 400px; height: 300px;
    background: radial-gradient(ellipse at 48% 30%, #fff8e6 0%, #f4d9a8 22%, #b99674 48%, #5b4f4a 80%, #3c3a3e 100%);
  }
  .photo--sunset::before {
    content: ""; position: absolute; left: 0; right: 0; top: 0; height: 60px;
    background: linear-gradient(180deg, #ffffff 0%, rgba(255,255,255,0) 100%);
  }
  .photo--firepit {
    left: 800px; top: 0; width: 400px; height: 700px;
    background: linear-gradient(180deg, #c9ccd2 0%, #8d939c 28%, #5c7a46 42%, #6f8f57 55%, #8c857a 72%, #6b645c 100%);
  }
  .bottom-band { position: absolute; left: 0; top: 0; width: 1200px; height: 927px; }
  .info-box {
    position: absolute; top: 55px; width: 290px;
    padding: 18px 14px 20px 22px;
    background: var(--box-blue); color: var(--white);
    font-family: "Open Sans", Arial, sans-serif;
    font-size: 13.4px; line-height: 18.8px;
  }
  .info-box--experience { left: 55px; height: 381px; }
  .info-box--diagnosis { left: 455px; height: 288px; background: var(--box-blue-solid); }
  .info-box--programming { left: 855px; height: 549px; }
  .info-box h2 {
    font-family: "Crimson Pro", Georgia, serif;
    font-weight: 600; font-size: 27px; line-height: 30px;
    letter-spacing: 0.2px; margin-bottom: 14px;
  }
  .info-box p + p { margin-top: 18.8px; }
  .service-list { list-style: none; }
  .service-list li { padding-left: 11px; position: relative; }
  .service-list li::before { content: "·"; position: absolute; left: 0; }
  .list-label { font-weight: 600; margin-top: 18.8px; }
</style>
</head>
<body>
  <main class="spread">
    <div class="photo photo--forest" role="img" aria-label="Photo of two people walking along a misty forest path"></div>
    <div class="photo photo--sunset" role="img" aria-label="Photo of a small group standing on a hilltop at sunset"></div>
    <div class="photo photo--firepit" role="img" aria-label="Photo of the facility's outdoor fire pit area with Adirondack chairs"></div>

    <svg class="bottom-band" viewBox="0 0 1200 927" aria-hidden="false">
      <defs>
        <linearGradient id="trailTone" x1="0" y1="0" x2="1" y2="0">
          <stop offset="0" stop-color="#2a2526"/>
          <stop offset="0.3" stop-color="#5a3324"/>
          <stop offset="0.5" stop-color="#7a4a2c"/>
          <stop offset="0.72" stop-color="#2c2d36"/>
          <stop offset="1" stop-color="#1d2434"/>
        </linearGradient>
        <linearGradient id="trailFade" x1="0" y1="0" x2="0" y2="1">
          <stop offset="0" stop-color="#1d2434" stop-opacity="0"/>
          <stop offset="1" stop-color="#1d2434" stop-opacity="0.85"/>
        </linearGradient>
      </defs>
      <g role="img" aria-label="Photo of a group walking down an autumn forest trail toward the light">
        <path d="M0 560 C 200 490, 420 520, 620 610 C 800 690, 980 740, 1200 640 L1200 927 L0 927 Z" fill="url(#trailTone)"/>
        <path d="M0 560 C 200 490, 420 520, 620 610 C 800 690, 980 740, 1200 640 L1200 927 L0 927 Z" fill="url(#trailFade)"/>
      </g>
      <path class="wave-green" d="M0 545 C 160 470, 380 470, 520 560 C 700 650, 940 700, 1200 605 L1200 625 C 960 710, 720 665, 540 580 C 390 510, 180 505, 0 572 Z" fill="var(--wave-green)"/>
      <path class="wave-blue" d="M0 572 C 200 505, 420 520, 620 610 C 800 690, 980 740, 1200 640 L1200 665 C 980 770, 780 720, 600 635 C 420 555, 200 540, 0 595 Z" fill="var(--wave-blue)"/>
    </svg>

    <section class="info-box info-box--experience">
      <h2>The Experience</h2>
      <p>Residential Treatment at Maple Hollow offers intensive structured treatment services for men and women suffering from substance abuse disorders in a 24-hour medically monitored Long-term residential treatment facility.</p>
      <p>Our treatment facilities offer clients the ability to feel welcomed, accepted and supported in a retreat like setting. Our multi-disciplinary team consists of Physicians, Therapists, Nurses, Case Managers, and other Recovery Support Specialists, allowing for each individual's physical, social, mental, and emotional development.</p>
    </section>

    <section class="info-box info-box--diagnosis">
      <h2>Dual Diagnosis</h2>
      <p>It is an unfortunate reality that many individuals who struggle with addiction are also faced with mental illness. Our residential treatment programs support dually-diagnosed individuals by providing onsite psychiatric evaluations, regular psychiatric follow-ups, medication management, and therapy services aimed at treating these symptoms as a part of the client's individualized treatment plan.</p>
    </section>

    <section class="info-box info-box--programming">
      <h2>Our Programming</h2>
      <p>Residential treatment programing provides comprehensive treatment for those struggling with drug and alcohol addiction along with those who are dually diagnosed with mental health issues as well. Residents will be able to experience an evidence-based program model inclusive of:</p>
      <ul class="service-list">
        <li>Comprehensive Evaluations</li>
        <li>Treatment Team Collaboration</li>
        <li>Medication Management</li>
        <li>Aftercare Planning</li>
        <li>Individual Therapy</li>
        <li>Family Therapy</li>
        <li>Group Therapy</li>
      </ul>
      <p class="list-label">Groups</p>
      <ul class="service-list">
        <li>Psychoeducational</li>
        <li>Psychotherapy</li>
        <li>Health &amp; Wellness</li>
        <li>Independent Living Skills</li>
        <li>Peer-Led (AA/NA)</li>
        <li>Grief &amp; Loss</li>
        <li>Codependency</li>
        <li>Stress Management</li>
      </ul>
    </section>
  </main>
</body>
</html>
```